Website for Party

Design a new website for PlumtreeGatherings.net
We have attached the new logos and please look at the website, and our facebook page: facebook.com/plumtreegatherings for inspiration
Updates

Hi Guys, please be original with all designs and images otherwise the design will be eliminated Thank you

some of your designs have too much happening in them, others make it clear that the designer has not yet read the brief fully

Please everyone be original!

```html
<!DOCTYPE html>
<html lang="en">
<head>
<meta charset="utf-8">
<title>PlumtreeGatherings.net — Epic Mixes</title>
<link rel="stylesheet" href="https://fonts.googleapis.com/css2?family=Jost:ital,wght@0,400;0,500;0,600;0,800;1,400&display=swap">
<style>
  :root {
    --red: #ff0000;
    --black: #000000;
    --white: #ffffff;
    --night: #050a18;
    --glow: #1e5cff;
  }
  * { box-sizing: border-box; margin: 0; padding: 0; }
  html, body { width: 741px; height: 1200px; overflow: hidden; background: var(--white); }
  body { position: relative; font-family: "Jost", "Futura", sans-serif; color: var(--white); }

  .site-header {
    position: absolute; top: 0; left: 0; width: 741px; height: 45px;
    background: var(--black); z-index: 2;
  }
  .brand {
    position: absolute; left: 8px; top: 16px; width: 52px;
    text-align: center; font-weight: 500; font-size: 10px; letter-spacing: 0.5px;
  }
  .main-nav { position: absolute; top: 17px; left: 0; width: 741px; }
  .main-nav a {
    position: absolute; color: var(--white); text-decoration: none;
    font-size: 11px; font-weight: 400; letter-spacing: 0.2px;
  }
  .search-button {
    position: absolute; right: 0; top: 0; width: 45px; height: 45px;
    background: var(--red); display: flex; align-items: center; justify-content: center;
  }

  .hero {
    position: absolute; top: 0; left: 0; width: 741px; height: 385px;
    background:
      radial-gradient(ellipse at 70% 40%, rgba(30,92,255,0.55), transparent 55%),
      radial-gradient(ellipse at 20% 75%, rgba(30,92,255,0.35), transparent 45%),
      radial-gradient(circle at 28% 66%, rgba(255,90,20,0.45), transparent 6%),
      linear-gradient(160deg, #0b1430 0%, var(--night) 60%, #000 100%);
  }
  .hero-title {
    position: absolute; left: 106px; top: 186px; width: 530px; height: 50px;
    background: var(--red); color: var(--white);
    font-weight: 800; font-size: 38px; line-height: 50px; text-align: center;
    letter-spacing: 0.5px; white-space: nowrap;
  }

  .feature-card {
    position: absolute; width: 200px; height: 254px;
    border-radius: 8px; overflow: hidden; background: var(--red);
  }
  .card-image { position: absolute; top: 0; left: 0; width: 200px; height: 196px; }
  .image-bar {
    background:
      radial-gradient(circle at 55% 45%, rgba(40,140,255,0.6), transparent 25%),
      radial-gradient(circle at 50% 58%, rgba(255,40,40,0.6), transparent 18%),
      radial-gradient(circle at 35% 30%, rgba(60,170,60,0.5), transparent 18%),
      var(--black);
  }
  .image-harbor {
    background: linear-gradient(180deg, #c9b9a6 0%, #e8b98a 20%, #6b7f95 42%, #2d4a70 70%, #1c3456 100%);
  }
  .image-carpet {
    background: radial-gradient(ellipse at 50% 70%, #d81010, #a00000 80%);
  }
  .card-label {
    position: absolute; left: 0; bottom: 0; width: 200px; height: 58px;
    display: flex; align-items: center; justify-content: center; text-align: center;
    font-weight: 500; font-size: 16px; line-height: 19px; text-transform: uppercase;
  }
  .card-tab {
    position: absolute; left: 84px; top: -7px; width: 32px; height: 8px;
    background: var(--red); border-radius: 3px 3px 0 0;
  }
  .card-tab svg { position: absolute; left: 8px; top: 1px; }
  .card-copy {
    position: absolute; top: 19px; left: 22px; width: 156px;
    font-style: italic; font-size: 13.3px; line-height: 15.8px; text-align: center;
  }
  .card-chevron { position: absolute; left: 84px; top: 3px; }

  .site-footer {
    position: absolute; top: 1035px; left: 0; width: 741px; height: 165px;
    background: var(--black); text-align: center;
  }
  .footer-brand {
    position: absolute; top: 32px; left: 0; width: 741px;
    font-weight: 500; font-size: 13px; letter-spacing: 0.5px;
  }
  .social-links {
    position: absolute; top: 77px; left: 300px; display: flex; gap: 2px;
  }
  .social-links span { display: block; width: 13px; height: 13px; }
  .footer-copy {
    position: absolute; top: 108px; left: 80px; width: 581px;
    font-size: 5px; line-height: 7.5px; text-align: center;
  }
  .footer-legal {
    position: absolute; top: 137px; left: 0; width: 741px;
    font-size: 5.5px; line-height: 7px;
  }
</style>
</head>
<body>

<header class="site-header">
  <div class="brand">Plumtree</div>
  <nav class="main-nav">
    <a href="#" style="left:304px">ABOUT</a>
    <a href="#" style="left:420px">FAQ</a>
    <a href="#" style="left:523px">TICKETS</a>
    <a href="#" style="left:629px">CONTACT</a>
  </nav>
  <div class="search-button">
    <svg width="16" height="18" viewBox="0 0 16 18" aria-label="Search">
      <circle cx="9" cy="6.5" r="4.8" fill="none" stroke="#fff" stroke-width="2"/>
      <line x1="6" y1="10.5" x2="2.5" y2="16" stroke="#fff" stroke-width="2" stroke-linecap="round"/>
    </svg>
  </div>
</header>

<section class="hero" role="img" aria-label="Close-up of a lit DJ mixing console with glowing blue knobs and faders">
  <h1 class="hero-title">EPIC MIXES BY DJ MARLO</h1>
</section>

<main>
  <article class="feature-card" style="left:33px; top:403px">
    <div class="card-image image-bar" role="img" aria-label="Layered colourful cocktail in a martini glass with fruit garnish on black"></div>
    <div class="card-label"><span class="card-tab"><svg width="16" height="6"><polyline points="1,5 8,1 15,5" fill="none" stroke="#fff" stroke-width="1"/></svg></span>Open Premium Bar</div>
  </article>
  <article class="feature-card" style="left:270px; top:403px">
    <div class="card-image image-harbor" role="img" aria-label="Aerial view of a city skyline and harbour at sunset"></div>
    <div class="card-label"><span class="card-tab"><svg width="16" height="6"><polyline points="1,5 8,1 15,5" fill="none" stroke="#fff" stroke-width="1"/></svg></span>Cruise Around<br>NYC Harbor</div>
  </article>
  <article class="feature-card" style="left:507px; top:403px">
    <svg class="card-chevron" width="32" height="8"><polyline points="1,1 16,7 31,1" fill="none" stroke="#ff5a5a" stroke-width="1.5"/></svg>
    <p class="card-copy">Arrive on the pier and walk down the red carpet with your group. A team of professional photographers will capture your red carpet grand entrance. All of the red carpet photos will be touched up by professional graphic artists and made available on the website and on Plumtree's event page after the night.</p>
    <div class="card-label">Red Carpet Entry</div>
  </article>

  <article class="feature-card" style="left:33px; top:700px">
    <div class="card-image image-bar" role="img" aria-label="Layered colourful cocktail in a martini glass with fruit garnish on black"></div>
    <div class="card-label"><span class="card-tab"><svg width="16" height="6"><polyline points="1,5 8,1 15,5" fill="none" stroke="#fff" stroke-width="1"/></svg></span>Open Premium Bar</div>
  </article>
  <article class="feature-card" style="left:270px; top:700px">
    <div class="card-image image-harbor" role="img" aria-label="Aerial view of a city skyline and harbour at sunset"></div>
    <div class="card-label"><span class="card-tab"><svg width="16" height="6"><polyline points="1,5 8,1 15,5" fill="none" stroke="#fff" stroke-width="1"/></svg></span>Cruise Around<br>NYC Harbor</div>
  </article>
  <article class="feature-card" style="left:507px; top:700px">
    <div class="card-image image-carpet" role="img" aria-label="Close-up of textured red carpet"></div>
    <div class="card-label"><span class="card-tab"><svg width="16" height="6"><polyline points="1,5 8,1 15,5" fill="none" stroke="#fff" stroke-width="1"/></svg></span>Red Carpet Entry</div>
  </article>
</main>

<footer class="site-footer">
  <div class="footer-brand">Plumtree</div>
  <div class="social-links" aria-label="Social links">
    <span style="background:#3b5b98"></span><span style="background:#33a8e0"></span><span style="background:#c9252c"></span><span style="background:#d64937"></span><span style="background:#555"></span><span style="background:#0e76a8"></span><span style="background:#517fa4"></span><span style="background:#f39c12"></span><span style="background:#c4302b"></span>
  </div>
  <p class="footer-copy">This is placeholder copy for the footer area of the site. Our team plans each evening on the water with care, from the first drink at the bar to the last song of the night. Book early to secure your place on deck, bring your friends and enjoy the skyline as the city lights come on. Guest lists close two days before each cruise and all tickets are final. Dress code applies for every event on board.</p>
  <p class="footer-legal">Terms &amp; Conditions<br>copyright 2014</p>
</footer>

</body>
</html>
```